Life and business Coaching Business Card and Logo

A new design for new company. We coach people to get the best out of themselves in business, life, health , family, career, relationships.
we work in Professional, executive, business and corporate environment. We use art and the processes of making art to work with getting people to delve into and change their mind maps or the way they are currently thinking so that they can move forward towards their goals strategically.
Updates

Project Deadline Extended
Reason: I have been laid up in bed with back problems and have just been able to get back to view designs. several are quiet good and I have given feedback today. I also want to take my project off refundable status as I will choose a design from this brief. regards Marisol

Target Market(s)

Professional artistic and bold energetic individuals

Industry/Entity Type

Health

Contact Information for Business Card

Vel5Mentoring, Marisol Drayke, Shaping Days Boldly,
Mob:0419586740, Ph: +61 8 95820647,
Professional, Executive, Business and Corporate Coach

Requirements
Must have
• a logo that can be used on all promotional and stationary material.
Should contain a person and be bold/colourful, simple and artistic.
Nice to have
• Room to place qualifications of Business

```html
<!DOCTYPE html>
<html lang="en">
<head>
<meta charset="utf-8">
<title>Vel5Mentoring Business Card</title>
<link rel="stylesheet" href="https://fonts.googleapis.com/css2?family=Days+One&display=swap">
<style>
  :root {
    --field-deep: #041a04;
    --field-mid: #0c4a0c;
    --field-bright: #2a9a1e;
    --panel-teal: #33b98a;
    --panel-teal-dark: #23906a;
    --stripe-teal: #3fcf98;
    --text-white: #ffffff;
    --brand-green: #9be22a;
    --glow: rgba(200, 255, 220, 0.7);
  }
  html, body {
    margin: 0;
    padding: 0;
    overflow: hidden;
    background: #ffffff;
  }
  .card {
    position: relative;
    width: 1200px;
    height: 741px;
    overflow: hidden;
    font-family: "Days One", sans-serif;
    color: var(--text-white);
  }
  .card-art {
    position: absolute;
    inset: 0;
  }
  .contact-block {
    position: absolute;
    left: 38px;
    top: 124px;
    font-size: 20px;
    line-height: 33.5px;
    text-transform: uppercase;
    letter-spacing: 0.2px;
  }
  .contact-block p { margin: 0; white-space: nowrap; }
  .brand {
    position: absolute;
    left: 0;
    width: 1200px;
    top: 418px;
    text-align: center;
    text-transform: uppercase;
  }
  .brand-name {
    font-size: 38px;
    color: var(--brand-green);
    letter-spacing: 0.5px;
    margin: 0;
    line-height: 44px;
  }
  .brand-tagline {
    font-size: 19px;
    margin: 6px 0 0;
    letter-spacing: 0.5px;
  }
  .services {
    position: absolute;
    top: 697px;
    left: 0;
    width: 1200px;
    height: 26px;
    margin: 0;
    padding: 0;
    list-style: none;
    text-transform: uppercase;
    font-size: 20px;
  }
  .services li {
    position: absolute;
    top: 0;
    white-space: nowrap;
    padding-left: 26px;
    line-height: 26px;
  }
  .services li::before {
    content: "";
    position: absolute;
    left: 0;
    top: 6px;
    width: 14px;
    height: 14px;
    background: var(--text-white);
    box-shadow: 0 0 12px 4px var(--glow);
  }
  .services .svc-professional { left: 216px; }
  .services .svc-executive { left: 467px; }
  .services .svc-business { left: 688px; }
  .services .svc-corporate { left: 862px; }
</style>
</head>
<body>
<div class="card">
  <svg class="card-art" width="1200" height="741" viewBox="0 0 1200 741" role="img" aria-label="Green honeycomb-textured background with teal panels and diagonal bands">
    <defs>
      <radialGradient id="fieldGlow" cx="50%" cy="52%" r="60%">
        <stop offset="0%" stop-color="var(--field-deep)"/>
        <stop offset="45%" stop-color="var(--field-mid)"/>
        <stop offset="100%" stop-color="var(--field-bright)"/>
      </radialGradient>
      <linearGradient id="panelFill" x1="0" y1="0" x2="0" y2="1">
        <stop offset="0%" stop-color="var(--panel-teal)"/>
        <stop offset="100%" stop-color="var(--panel-teal-dark)"/>
      </linearGradient>
      <clipPath id="stripeZone">
        <polygon points="906,190 1082,125 1082,672 906,672"/>
      </clipPath>
    </defs>

    <rect class="field" width="1200" height="741" fill="url(#fieldGlow)"/>

    <!-- top band with right-side drop -->
    <polygon class="top-band" fill="url(#panelFill)"
      points="0,0 1200,0 1200,68 1108,68 1082,108 895,108 855,68 0,68"/>

    <!-- contact panel -->
    <polygon class="contact-panel" fill="url(#panelFill)"
      points="0,108 303,108 360,162 360,294 0,294"/>

    <!-- right stripe column -->
    <g class="stripe-column" clip-path="url(#stripeZone)">
      <rect x="906" y="120" width="176" height="560" fill="#0f5210"/>
      <g fill="var(--stripe-teal)">
        <polygon points="906,230 1082,120 1082,190 906,300"/>
        <polygon points="906,370 1082,260 1082,330 906,440"/>
        <polygon points="906,510 1082,400 1082,470 906,580"/>
        <polygon points="906,650 1082,540 1082,610 906,720"/>
      </g>
    </g>
    <rect class="stripe-edge" x="1082" y="108" width="118" height="564" fill="var(--field-bright)" opacity="0.6"/>

    <!-- bottom band with left rise -->
    <polygon class="bottom-band" fill="url(#panelFill)"
      points="0,632 270,632 314,672 1200,672 1200,741 0,741"/>
  </svg>

  <div class="contact-block">
    <p class="contact-company">Vel5Mentoring</p>
    <p class="contact-name">Marisol Drayke</p>
    <p class="contact-tagline">Shaping Days Boldly</p>
    <p class="contact-mobile">Mob:0419586740</p>
    <p class="contact-phone">Ph: +61 8 95820647</p>
  </div>

  <div class="brand">
    <p class="brand-name">Vel5Mentoring</p>
    <p class="brand-tagline">Shaping Days Boldly</p>
  </div>

  <ul class="services">
    <li class="svc-professional">Professional</li>
    <li class="svc-executive">Executive</li>
    <li class="svc-business">Business</li>
    <li class="svc-corporate">Corporate Coach</li>
  </ul>
</div>
</body>
</html>
```